Silicone product manufacturer needs name card

we are a silicone proudct manufacturer, need a name card.
Updates

Dear All, Pls use the following information for the name card. Maris Odell Marketing Manager Mobile : HK (852) 64839205 : CN (86) 13957204416 Tel : 852-24776150 Fax : 852-28364471 Rm705,7/F, Lok Tin Ind. Ctr., 24-26 Pak Fung St., Kwun Tong, HK China Office : Tel:86-796-85302617 Fax : 86-769-83651274 5-6/F, Rui Kang Building, No. 47 BeiLin Road, Shi Pai Wan Town, Dong Guan City, PRC China Factory Norvik Technology Ltd Tai Lun Technology Ltd Mei Sun Fat (F.S) Silicone Products Co. Ltd Pelvane Technology Ltd Slogan on the name card : We are your best Business Partner With ISO9001 / ISO14001 / TS16949 LOGO Any query, pls contact me at marisodell@qorvent-mail.net Thanks, maris

Reason: Dear All, Still can't choose the right one. Thanks, Maris

Reason: still not confirm

Reason: working on revision. thanks

Reason: revising the design with designer. thanks

Reason: revising with designer ! thanks

Industry/Entity Type

Manufacturer

```html
<!DOCTYPE html>
<html lang="en">
<head>
<meta charset="utf-8">
<title>Qorvent Technology Limited – Name Card</title>
<link rel="stylesheet" href="https://fonts.googleapis.com/css2?family=Barlow:wght@300;400;600&display=swap">
<style>
  :root {
    --bg: #e7e8ea;
    --cyan: #22b8d1;
    --cyan-light: #3fd3e6;
    --blue: #0d4aa8;
    --navy: #0b1f78;
    --ink: #2b2f36;
    --green: #7a9a1c;
    --card-white: #f4f5f6;
    --rule-blue: #1b3f8f;
  }
  * { box-sizing: border-box; margin: 0; padding: 0; }
  html, body { width: 1200px; height: 900px; overflow: hidden; }
  body {
    background: var(--bg);
    font-family: "Barlow", Arial, sans-serif;
    display: flex;
    align-items: center;
    justify-content: center;
    gap: 120px;
  }
  .card {
    width: 340px;
    height: 580px;
    position: relative;
    box-shadow: 0 8px 24px rgba(0,0,0,0.18);
    overflow: hidden;
  }

  /* Front */
  .card-front {
    background: radial-gradient(circle at 35% 25%, var(--cyan-light) 0%, var(--cyan) 35%, var(--blue) 80%, var(--navy) 100%);
    color: #fff;
  }
  .brand {
    position: absolute;
    top: 120px;
    left: 40px;
    right: 40px;
    display: flex;
    align-items: center;
    gap: 14px;
  }
  .brand-dot {
    width: 34px; height: 34px;
    border-radius: 50%;
    background: var(--navy);
    flex: none;
  }
  .brand-name {
    font-weight: 600;
    font-size: 30px;
    line-height: 1.05;
    color: var(--navy);
  }
  .slogan-band {
    position: absolute;
    top: 330px;
    left: 0;
    right: 0;
    height: 96px;
    background: var(--navy);
    display: flex;
    flex-direction: column;
    justify-content: center;
    padding-left: 40px;
  }
  .slogan {
    font-weight: 300;
    font-size: 21px;
    letter-spacing: 1px;
    line-height: 1.2;
    color: var(--cyan-light);
    text-transform: uppercase;
  }
  .certs {
    position: absolute;
    bottom: 34px;
    left: 40px;
    font-weight: 300;
    font-size: 12px;
    letter-spacing: 0.5px;
    color: #dbe6ff;
  }

  /* Back */
  .card-back {
    background: var(--card-white);
    color: var(--ink);
    padding: 28px 30px;
  }
  .back-brand {
    display: flex;
    align-items: center;
    gap: 8px;
    margin-bottom: 26px;
  }
  .back-brand .brand-dot { width: 16px; height: 16px; }
  .back-brand .brand-name { font-size: 15px; }
  .person-name {
    font-weight: 300;
    font-size: 22px;
    letter-spacing: 1px;
    color: var(--cyan);
    text-transform: uppercase;
  }
  .person-title {
    font-size: 14px;
    font-weight: 400;
    margin-bottom: 10px;
  }
  .info { font-size: 12.5px; line-height: 1.35; }
  .label-cyan { color: var(--cyan); text-transform: uppercase; }
  .label-green { color: var(--green); }
  .section-title { color: var(--green); font-weight: 400; }
  .mobile-row { display: flex; gap: 4px; }
  .rule {
    height: 1.5px;
    margin: 14px 0;
  }
  .rule-cyan { background: linear-gradient(90deg, var(--rule-blue), var(--cyan)); }
  .rule-green { background: linear-gradient(90deg, var(--green), #b6c94a); }
  .rule-blue { background: linear-gradient(90deg, var(--rule-blue), var(--cyan)); }
  .spacer { height: 8px; }
</style>
</head>
<body>

  <section class="card card-front" aria-label="Card front">
    <div class="brand">
      <span class="brand-dot"></span>
      <span class="brand-name">Qorvent Technology Limited</span>
    </div>
    <div class="slogan-band">
      <p class="slogan">We are your best</p>
      <p class="slogan">Business partner</p>
    </div>
    <p class="certs">ISO9001 / ISO14001 / TS16949</p>
  </section>

  <section class="card card-back" aria-label="Card back">
    <div class="back-brand">
      <span class="brand-dot"></span>
      <span class="brand-name">Qorvent</span>
    </div>

    <h1 class="person-name">Maris Odell</h1>
    <p class="person-title">Marketing Manager</p>
    <div class="info">
      <div class="mobile-row">
        <span class="label-cyan">Mobile:</span>
        <span>HK (852) 64839205<br>CN (86) 13957204416</span>
      </div>
    </div>

    <div class="rule rule-cyan"></div>

    <div class="info">
      <p class="section-title">Hong Kong Head Office</p>
      <p><span class="label-green">TEL:</span> 852-24776150</p>
      <p><span class="label-green">FAX:</span> 852-28364471</p>
      <div class="spacer"></div>
      <p>Rm705,7/F, Lok Tin Ind. Ctr.,</p>
      <p>24-26 Pak Fung St., Kwun Tong</p>
    </div>

    <div class="rule rule-green"></div>

    <div class="info">
      <p class="section-title">HK China Office</p>
      <p><span class="label-green">TEL:</span> 86-796-85302617</p>
      <p><span class="label-green">FAX:</span> 86-769-83651274</p>
      <div class="spacer"></div>
      <p>5-6/F, Rui Kang Building,</p>
      <p>No. 47 BeiLin Road,</p>
      <p>Shi Pai Wan Town, Dong Guan City</p>
    </div>

    <div class="rule rule-blue"></div>

    <div class="info">
      <p>PRC China Factory Norvik Technology</p>
      <p>Ltd Tai Lun Technology</p>
      <p>Ltd Mei Sun Fat (F.S) Silicone</p>
      <p>Products Co.</p>
      <p>Ltd Pelvane Technology Ltd</p>
    </div>
  </section>

</body>
</html>
```